TerraLume Business Card Design Project

We need a business card design for a new company called "TerraLume Systems". TerraLume provides 3D visualization software for subsurface oil and gas data so you can make confident downhole decisions.

Our goal is to provide easy to understand big pictures of your data so your can make confident planning decisions.

Our tagline is
SEAMLESS DATA SHARING. EFFECTIVE COLLABORATION. CONFIDENT DECISION-MAKING

Check out http://www.terralume-example.com for more ideas.

The design should promote a technology company that delivers web-based solutions focused on photo-realistic 3D graphics.

The colors from our existing logo (attached) are one option but not a requirement. The design SHOULD NOT use the existing logo.

The design should be two sided and full color. If you require any special print considerations (example: paper type, matte finish, metallic ink, etc) please provide detailed comments. Please also specify any desired details such as rounding of corners, etc.

IF YOU USE BLACK our printer states "We recommend using CMYK black (0, 0, 0, 100) or for a rich black (60, 40, 40, 100). Ensure your artwork is in CMYK mode before adjusting the black."

For design purposes you can use the following contact information

name: Harlan Pike
title: founder
phone: 555.987.6543
email: harlan@terralume-example.com

company information
TerraLume is our "branded" name
"TerraLume Systems" is our official name
www.terralume-example.com

address:
Suite 720
482 Birchmont Avenue SW
Calgary, AB, Canada
T3K 4R8

Target Market(s)

Companies spend a lot of time collecting, organizing and analyzing data but it's really hard to to get a big picture view of current and planned projects, especially in context to existing wellbores, geology and downhole equipment

TerraLume enables you to explore the big picture in an immersive, 3D environment. Our goal is to help transform you rich data into an easily understood picture, to make confident planning decisions and anticipate trouble events before the expensive execution phase.

Industry/Entity Type

Oil And Gas

Requirements
Must have
• The business card design should be sized to a standard 3.5 x 2 inches and print ready. See the attachment for a sample sized card
It MUST meet these requirements:
Exported as PDF file with two pages:
page 1: front design
page 2: back design
All Images must be 300ppi or higher (at 100%)
CMYK colour mode
0.125 inches of bleed on all sides (0.25 inches additional width and height)
0.125 inch safety margin (inside trim line)

```html
<!DOCTYPE html>
<html lang="en">
<head>
<meta charset="utf-8">
<title>TerraLume Systems – Business Card Front</title>
<link rel="stylesheet" href="https://fonts.googleapis.com/css2?family=Open+Sans:wdth,wght@75..100,400;75..100,700&display=swap">
<style>
  :root {
    --paper: #ffffff;
    --ink: #111111;
    --lime: #88ff00;
    --brand-green: #3bf018;
    --crop: #000000;
  }
  html, body {
    margin: 0;
    padding: 0;
    width: 1200px;
    height: 759px;
    overflow: hidden;
    background: var(--paper);
  }
  .card {
    position: relative;
    width: 1200px;
    height: 759px;
    background: var(--paper);
    font-family: "Open Sans", Arial, sans-serif;
    color: var(--ink);
  }
  .card-art {
    position: absolute;
    inset: 0;
    width: 1200px;
    height: 759px;
  }
  .brand-name {
    position: absolute;
    right: 165px;
    top: 236px;
    margin: 0;
    font-size: 78px;
    font-weight: 700;
    font-stretch: 75%;
    line-height: 1;
    letter-spacing: 1px;
    color: var(--brand-green);
  }
  .tagline {
    position: absolute;
    left: 264px;
    top: 389px;
    margin: 0;
    font-size: 26.5px;
    font-weight: 400;
    letter-spacing: 2.2px;
    line-height: 39.5px;
    text-transform: uppercase;
  }
  .tagline span { display: block; }
  .descriptor {
    position: absolute;
    left: 125px;
    top: 525px;
    margin: 0;
    font-size: 27.5px;
    font-weight: 400;
    letter-spacing: -0.2px;
    white-space: nowrap;
  }
</style>
</head>
<body>
  <main class="card">
    <svg class="card-art" viewBox="0 0 1225 775" preserveAspectRatio="none" aria-hidden="true">
      <defs>
        <linearGradient id="rim-shade" x1="180" y1="0" x2="720" y2="0" gradientUnits="userSpaceOnUse">
          <stop offset="0" stop-color="#ffffff"/>
          <stop offset="1" stop-color="#000000"/>
        </linearGradient>
        <clipPath id="trim-area">
          <rect x="88" y="0" width="1137" height="775"/>
        </clipPath>
      </defs>
      <g clip-path="url(#trim-area)">
        <ellipse class="oval-rim" cx="558" cy="492" rx="468" ry="148" fill="url(#rim-shade)"/>
        <ellipse class="oval-field" cx="553" cy="497" rx="467" ry="135" fill="var(--lime)"/>
      </g>
      <g class="crop-marks" stroke="var(--crop)" stroke-width="1">
        <line x1="88" y1="0" x2="88" y2="62"/>
        <line x1="1138" y1="0" x2="1138" y2="62"/>
        <line x1="0" y1="87" x2="62" y2="87"/>
        <line x1="1163" y1="87" x2="1225" y2="87"/>
        <line x1="0" y1="688" x2="62" y2="688"/>
        <line x1="1163" y1="688" x2="1225" y2="688"/>
        <line x1="88" y1="713" x2="88" y2="775"/>
        <line x1="1138" y1="713" x2="1138" y2="775"/>
      </g>
    </svg>

    <h1 class="brand-name">TERRALUME</h1>

    <p class="tagline">
      <span>Seamless data sharing.</span>
      <span>Effective collaboration.</span>
      <span>Confident decision-making</span>
    </p>

    <p class="descriptor">3D visualization software for subsurface oil and gas data</p>
  </main>
</body>
</html>
```